Not-for-profit Community Law Business Card

Not-for-Profit community law firm are looking for new business card design to accompany a new logo.
The cards are to assist the organisation in reaching their strategic objective of generating greater networking amongst the community; specifically with other service providers, clients, and community influencers.
It should stand out. Be professional, strong, creative, clear in detail. The logo should be a major feature of the design.
Updates

Hi All,

Thank you for the submissions so far. I have uploaded the logo and colour details again, as requested. If you have any further issues downloading them or need a different format please contact me on jess_harlow@bvm.net.au

Kind regards,

Industry/Entity Type

Law Firm

Requirements
Must have
• Logo (attached)
Person's name
Position
Phone
Fax
Email
PO Box address
Website
Colours from the logo.

```html
<!DOCTYPE html>
<html lang="en">
<head>
<meta charset="utf-8">
<title>Harbour Point Legal Centre – Business Card</title>
<link href="https://fonts.googleapis.com/css2?family=Arimo:wght@400;700&display=swap" rel="stylesheet">
<style>
  :root {
    --page: #ffffff;
    --card-centre: #ffffff;
    --card-edge: #dff0fa;
    --card-border: #a9d6ee;
    --card-shadow: #5d93b0;
    --brand-blue: #1b6fb8;
    --name-blue: #1a72b8;
    --position-navy: #2b3a8a;
    --detail-blue: #1f78bf;
    --icon-navy: #2a4c94;
  }
  * { margin: 0; padding: 0; box-sizing: border-box; }
  html, body {
    width: 758px; height: 1200px; overflow: hidden;
    background: var(--page);
    font-family: "Arimo", Arial, sans-serif;
  }
  .canvas { position: relative; width: 758px; height: 1200px; }
  .card {
    position: absolute; left: 64px; top: 33px; width: 656px; height: 1132px;
    border: 1.5px solid var(--card-border);
    border-radius: 0 64px 0 64px;
    background: radial-gradient(ellipse 60% 50% at 50% 44%, var(--card-centre) 0%, var(--card-centre) 25%, var(--card-edge) 100%);
    box-shadow: 3px 3px 0 var(--card-shadow);
  }
  .brand {
    position: absolute; left: 140px; top: 130px;
    display: flex; align-items: center; gap: 18px;
  }
  .brand-mark {
    width: 92px; height: 92px; border-radius: 50%;
    background: var(--brand-blue);
  }
  .brand-name {
    color: var(--brand-blue); font-weight: 700; text-transform: uppercase;
    line-height: 1.15;
  }
  .brand-name .line-main { display: block; font-size: 32px; letter-spacing: 0.5px; }
  .brand-name .line-sub { display: block; font-size: 17px; letter-spacing: 1.5px; text-align: right; }
  .centre-text { position: absolute; left: 64px; width: 656px; text-align: center; }
  .person-name { top: 414px; font-size: 46px; font-weight: 700; color: var(--name-blue); letter-spacing: 0.5px; }
  .person-position { top: 484px; font-size: 32px; color: var(--position-navy); }
  .postal-address { top: 674px; font-size: 31px; color: var(--detail-blue); }
  .contact-line {
    display: flex; justify-content: center; align-items: center; gap: 8px;
    font-size: 33px; color: var(--detail-blue);
  }
  .contact-phone { top: 892px; }
  .contact-email { top: 946px; }
  .contact-web { top: 997px; }
  .contact-line svg { fill: var(--icon-navy); flex: none; }
</style>
</head>
<body>
<main class="canvas">
  <section class="card">
  </section>

  <header class="brand">
    <div class="brand-mark"></div>
    <div class="brand-name">
      <span class="line-main">Harbour Point</span>
      <span class="line-sub">Legal Centre Inc.</span>
    </div>
  </header>

  <h1 class="centre-text person-name">NAME</h1>
  <p class="centre-text person-position">Position</p>
  <p class="centre-text postal-address">Adress and Po Box</p>

  <p class="centre-text contact-line contact-phone">
    <svg width="28" height="28" viewBox="0 0 24 24" aria-hidden="true"><path d="M6.6 10.8a15.1 15.1 0 0 0 6.6 6.6l2.2-2.2c.3-.3.7-.4 1-.2 1.1.4 2.3.6 3.6.6.6 0 1 .4 1 1V20c0 .6-.4 1-1 1A17 17 0 0 1 3 4c0-.6.4-1 1-1h3.5c.6 0 1 .4 1 1 0 1.3.2 2.5.6 3.6.1.3 0 .7-.2 1z"/></svg>
    <span>Phone Nnumber</span>
  </p>
  <p class="centre-text contact-line contact-email">
    <svg width="30" height="22" viewBox="0 0 30 22" aria-hidden="true"><rect x="0" y="2" width="30" height="19" rx="1.5"/><path d="M1 3l14 9 14-9" fill="none" stroke="#ffffff" stroke-width="2"/></svg>
    <span>email@</span>
  </p>
  <p class="centre-text contact-line contact-web">
    <svg width="24" height="24" viewBox="0 0 24 24" aria-hidden="true"><g fill="none" stroke="#2a4c94" stroke-width="1.8"><circle cx="12" cy="12" r="10"/><ellipse cx="12" cy="12" rx="4.5" ry="10"/><path d="M2 12h20M4 6.5h16M4 17.5h16"/></g></svg>
    <span>www.website.com</span>
  </p>
</main>
</body>
</html>
```